Terra Swift Business Card Design

We need to improve the design of our current business card. We are a erosion control, hydro seeding company that serves many markets. We are attaching the current business card and our logo as reference. You may also visit our site at www.terraswiftllc.example to reference.

```html
<!DOCTYPE html>
<html lang="en">
<head>
<meta charset="utf-8">
<title>Terra Swift Business Card</title>
<link rel="stylesheet" href="https://fonts.googleapis.com/css2?family=Open+Sans:wght@400;600;700;800&display=swap">
<style>
  :root {
    --backdrop: #262626;
    --card: #ffffff;
    --green-dark: #0b6b3f;
    --green-light: #19ad6e;
    --ink: #2f2f2f;
  }
  * { margin: 0; padding: 0; box-sizing: border-box; }
  html, body { width: 1200px; height: 1059px; overflow: hidden; }
  body {
    background: var(--backdrop);
    font-family: "Open Sans", Arial, sans-serif;
    color: var(--ink);
    position: relative;
  }
  .card {
    position: absolute;
    left: 255px;
    width: 692px;
    height: 393px;
    background: var(--card);
    border-radius: 22px;
    box-shadow: 0 8px 20px rgba(0,0,0,0.55);
  }
  .card--front { top: 88px; }
  .card--back { top: 548px; }

  .brand {
    position: absolute;
    display: flex;
    align-items: center;
    gap: 10px;
    font-weight: 800;
    color: var(--green-dark);
    white-space: nowrap;
    letter-spacing: -0.5px;
  }
  .brand__dot {
    border-radius: 50%;
    background: var(--green-dark);
    flex: none;
  }
  .card--front .brand { left: 40px; top: 170px; font-size: 40px; }
  .card--front .brand__dot { width: 22px; height: 22px; }
  .card--back .brand {
    left: 0; right: 0; top: 150px;
    justify-content: center;
    font-size: 76px;
    gap: 16px;
  }
  .card--back .brand__dot { width: 40px; height: 40px; }

  .details {
    position: absolute;
    left: 403px;
    top: 74px;
    height: 246px;
    border-left: 2px solid var(--green-light);
    padding-left: 19px;
  }
  .details__name {
    font-size: 27px;
    font-weight: 700;
    line-height: 1;
    color: var(--green-dark);
    margin-top: -4px;
    letter-spacing: -0.3px;
  }
  .details__name span { color: var(--green-light); }
  .details__role { font-size: 19px; margin-top: 6px; }
  .contact { list-style: none; margin-top: 14px; }
  .contact li {
    display: flex; align-items: center; gap: 6px;
    font-size: 19px; line-height: 24.5px;
  }
  .contact svg { width: 17px; height: 17px; fill: var(--green-dark); flex: none; }
  .address { font-style: normal; font-size: 19px; line-height: 24.5px; margin-top: 10px; }
</style>
</head>
<body>
  <section class="card card--front">
    <div class="brand"><span class="brand__dot"></span>Terra Swift</div>
    <div class="details">
      <h1 class="details__name">DANIEL <span>HART</span></h1>
      <p class="details__role">Managing Director</p>
      <ul class="contact">
        <li><svg viewBox="0 0 24 24"><path d="M6.6 10.8a15.1 15.1 0 0 0 6.6 6.6l2.2-2.2c.3-.3.7-.4 1-.2 1.1.4 2.3.6 3.6.6.6 0 1 .4 1 1V20c0 .6-.4 1-1 1A17 17 0 0 1 3 4c0-.6.4-1 1-1h3.5c.6 0 1 .4 1 1 0 1.3.2 2.5.6 3.6.1.3 0 .7-.2 1z"/></svg>(555) 014-2286</li>
        <li><svg viewBox="0 0 24 24"><path d="M8 2h9v6h3a2 2 0 0 1 2 2v12H8zM10 4v4h5V4zM10 12h2v2h-2zm4 0h2v2h-2zm4 0h2v2h-2zm-8 4h2v2h-2zm4 0h2v2h-2zm4 0h2v2h-2zM2 8h5v14H2z"/></svg>(555) 014-2285</li>
        <li><svg viewBox="0 0 24 24"><path d="M2 6h20v13H2zm2 2v.4l8 5.2 8-5.2V8zm0 2.8V17h16v-6.2l-8 5.2z"/></svg>info@terraswiftllc.example</li>
        <li><svg viewBox="0 0 24 24"><path d="M12 2a10 10 0 1 0 0 20 10 10 0 0 0 0-20zm-1 17.9A8 8 0 0 1 4.2 10L9 14.8v1a2 2 0 0 0 2 2zm6.9-2.5A2 2 0 0 0 16 16h-1v-3a1 1 0 0 0-1-1H8v-2h2a1 1 0 0 0 1-1V7h2a2 2 0 0 0 2-2v-.4a8 8 0 0 1 2.9 12.8z"/></svg>www.terraswiftllc.example</li>
      </ul>
      <address class="address">Corporate Headquarters<br>72 Marsh Hollow Lane<br>Linden Creek, NC 28400</address>
    </div>
  </section>

  <section class="card card--back">
    <div class="brand"><span class="brand__dot"></span>Terra Swift</div>
  </section>
</body>
</html>
```